VELMAR WEBSITE

need to create a new website for VELMAR ltd
the company deals with all aspects of safety products & safety wear
we need a simple website to show
ideas can be taken from following website whose products we shall distribute in kenya
www.qtw.co.uk
www.brovik.eu
www.tormanhardgear.com
www.qalvenworks.co.za

we need following tabs
1) home - basic company information
2) products - broken down to following categories ie gloves, head protection, ear protection, mouth protection, foot protection
3) contacts

the company profile is a reputable company dealing with all aspects of safety, HSE (health and safety equipment), and PPE (personal protective equipment)

the website should have the brovik logo for which we are an authorized distributor.
the brovi industrial range writeup can be picked from their website

Dear Designers, i shall be able to choose a final design in 2 weeks, sorry i have not been able to finalise this due to a personal reason

Target Market(s)

the buyers are all types of industry who care for their employees safety

Industry/Entity Type

Industrial

Requirements
Must have
• clean look, fresh look, user freindly
Nice to have
• clear images, quick links etc

```html
<!DOCTYPE html>
<html lang="en">
<head>
<meta charset="utf-8">
<title>VELMAR – Safety Products</title>
<link rel="stylesheet" href="https://fonts.googleapis.com/css2?family=Open+Sans:ital,wght@0,400;0,600;0,700;0,800;1,400&display=swap">
<style>
  :root {
    --navy-deep: #0a2a4f;
    --navy: #0f4a86;
    --blue-bright: #1c7fc0;
    --header-light: #b9c5d3;
    --strip: #7f93aa;
    --logo-ink: #1a3550;
    --logo-square: #f2b51c;
    --brand-partner: #1a6fb5;
    --nav-top: #f3f2ec;
    --nav-bottom: #d2d1c4;
    --nav-ink: #3a3a3a;
    --nav-active: #1aa3d8;
    --ink: #2c2c2c;
    --body-text: #9a9a9a;
    --panel-bg: #e4e4e4;
    --white: #ffffff;
  }
  * { box-sizing: border-box; margin: 0; padding: 0; }
  html, body { width: 1200px; height: 1200px; overflow: hidden; }
  body {
    position: relative;
    font-family: "Open Sans", Arial, sans-serif;
    background: linear-gradient(180deg, #ffffff 0%, #f4f4f4 60%, #ffffff 100%);
    color: var(--ink);
  }
  .site-header {
    position: absolute; left: 0; top: 0; width: 1200px; height: 292px;
  }
  .header-band { position: absolute; left: 0; top: 0; width: 1200px; height: 292px; }
  .logo {
    position: absolute; left: 16px; top: 118px;
    display: flex; align-items: center; gap: 14px;
    font-weight: 800; font-size: 62px; letter-spacing: 2px; color: var(--logo-ink);
    line-height: 1;
  }
  .logo-square { width: 44px; height: 44px; background: var(--logo-square); }
  .tagline {
    position: absolute; color: var(--white); font-style: italic; font-size: 35px; line-height: 1;
  }
  .tagline-first { left: 403px; top: 92px; }
  .tagline-second { left: 565px; top: 138px; }
  .distributor-note {
    position: absolute; left: 877px; top: 42px;
    font-size: 15px; font-weight: 700; color: var(--white);
  }
  .partner-name {
    position: absolute; left: 910px; top: 80px;
    font-size: 66px; font-weight: 600; color: var(--brand-partner); line-height: 1;
    letter-spacing: -1px;
  }
  .alphabet {
    position: absolute; left: 454px; top: 258px;
    display: flex; gap: 3px; list-style: none;
  }
  .alphabet a { color: var(--white); font-size: 13.5px; text-decoration: underline; }
  .search {
    position: absolute; left: 938px; top: 252px; width: 218px; height: 34px;
    background: var(--white); border: 2px solid #c9d2dc;
    font-style: italic; font-size: 19px; color: #b5b5b5; padding: 2px 8px;
  }
  .main-nav {
    position: absolute; left: 34px; top: 298px; width: 918px; height: 73px;
    background: linear-gradient(180deg, var(--nav-top), var(--nav-bottom));
    box-shadow: 0 4px 10px rgba(0,0,0,0.12);
  }
  .main-nav a {
    position: absolute; top: 18px; font-size: 27px; color: var(--nav-ink); text-decoration: none;
  }
  .main-nav a.is-active { color: var(--nav-active); }
  .category-menu {
    position: absolute; left: 34px; top: 371px; width: 333px; height: 295px;
    background: var(--white);
    box-shadow: 4px 6px 14px rgba(0,0,0,0.18);
    list-style: none;
  }
  .category-menu li {
    position: absolute; left: 61px; font-size: 26px; color: #1f1f1f;
  }
  .chevron { position: absolute; left: 14px; top: 20px; }
  .about {
    position: absolute; left: 413px; top: 428px; width: 485px;
  }
  .about h1 { font-weight: 400; font-size: 36px; color: var(--ink); }
  .gallery { position: absolute; top: 86px; left: 0; display: flex; gap: 24px; }
  .gallery-tile {
    width: 139px; height: 136px;
    background: linear-gradient(135deg, #e9e9e9 0%, #c4c4c4 100%);
  }
  .about p {
    position: absolute; left: 0; width: 485px;
    font-size: 17px; line-height: 23.4px; color: var(--body-text); text-align: justify;
  }
  .about .para-one { top: 270px; }
  .about .para-two { top: 431px; }
  .whats-new {
    position: absolute; left: 932px; top: 403px; width: 228px; height: 602px;
    background: var(--panel-bg);
  }
  .whats-new h2 {
    font-weight: 400; font-size: 32px; text-align: center; margin-top: 6px; color: #333;
  }
  .news-item { position: absolute; left: 8px; width: 212px; }
  .news-date { font-size: 10px; color: #333; }
  .news-text { font-size: 11.5px; line-height: 14px; color: #a6a6a6; text-align: justify; margin-top: 8px; }
  .news-more { font-size: 10px; color: #333; margin-top: 2px; }
  .site-footer {
    position: absolute; left: 0; top: 1113px; width: 1200px; height: 87px;
    background: radial-gradient(ellipse at 50% 0%, var(--blue-bright) 0%, var(--navy) 40%, var(--navy-deep) 100%);
    color: var(--white); font-size: 20px; text-align: center; line-height: 87px;
  }
</style>
</head>
<body>
  <header class="site-header">
    <svg class="header-band" width="1200" height="292" viewBox="0 0 1200 292" aria-hidden="true">
      <defs>
        <linearGradient id="headerBlue" x1="0" y1="0" x2="1" y2="0.3">
          <stop offset="0" stop-color="#2f8ccc"/>
          <stop offset="0.45" stop-color="#0f5a98"/>
          <stop offset="1" stop-color="#0a2a4f"/>
        </linearGradient>
        <linearGradient id="stripGrad" x1="0" y1="0" x2="1" y2="0">
          <stop offset="0" stop-color="#9aa9bb"/>
          <stop offset="1" stop-color="#6d82a0"/>
        </linearGradient>
        <radialGradient id="logoDisc" cx="0.3" cy="0.4" r="0.8">
          <stop offset="0" stop-color="#d6dde6"/>
          <stop offset="1" stop-color="#aebccc"/>
        </radialGradient>
      </defs>
      <rect x="0" y="0" width="1200" height="242" fill="url(#headerBlue)"/>
      <rect x="0" y="242" width="1200" height="50" fill="url(#stripGrad)"/>
      <path d="M0 0 H300 A230 230 0 0 1 365 230 Q358 266 340 292 H0 Z" fill="url(#logoDisc)"/>
    </svg>
    <div class="logo"><span class="logo-square"></span>VELMAR</div>
    <p class="tagline tagline-first">When you care for safety...</p>
    <p class="tagline tagline-second">we are here to help.</p>
    <p class="distributor-note">We are an authorized distributor for</p>
    <p class="partner-name">Brovik</p>
    <ul class="alphabet">
      <li><a href="#">A</a></li><li><a href="#">B</a></li><li><a href="#">C</a></li><li><a href="#">D</a></li>
      <li><a href="#">E</a></li><li><a href="#">F</a></li><li><a href="#">G</a></li><li><a href="#">H</a></li>
      <li><a href="#">I</a></li><li><a href="#">J</a></li><li><a href="#">K</a></li><li><a href="#">L</a></li>
      <li><a href="#">M</a></li><li><a href="#">N</a></li><li><a href="#">O</a></li><li><a href="#">P</a></li>
      <li><a href="#">Q</a></li><li><a href="#">R</a></li><li><a href="#">S</a></li><li><a href="#">T</a></li>
      <li><a href="#">U</a></li><li><a href="#">V</a></li><li><a href="#">W</a></li><li><a href="#">X</a></li>
      <li><a href="#">Y</a></li><li><a href="#">Z</a></li>
    </ul>
    <div class="search">search...</div>
  </header>

  <nav class="main-nav">
    <a href="#" style="left:51px">Products Categories</a>
    <a href="#" class="is-active" style="left:379px">About us</a>
    <a href="#" style="left:559px">Our Partner</a>
    <a href="#" style="left:775px">Contact</a>
  </nav>

  <ul class="category-menu">
    <li style="top:20px">
      <svg class="chevron" width="22" height="22" viewBox="0 0 22 22" aria-hidden="true" style="left:-47px;top:6px">
        <circle cx="11" cy="11" r="10" fill="#f2f2f2" stroke="#d0d0d0"/>
        <path d="M9 6 L14 11 L9 16" fill="none" stroke="#333" stroke-width="2"/>
      </svg>Gloves</li>
    <li style="top:71px">Foot Protection</li>
    <li style="top:123px">Mouth Protection</li>
    <li style="top:174px">Head Protection</li>
    <li style="top:224px">Ear Protection</li>
  </ul>

  <main class="about">
    <h1>About us</h1>
    <div class="gallery">
      <div class="gallery-tile" role="img" aria-label="Safety gloves product photo"></div>
      <div class="gallery-tile" role="img" aria-label="Protective footwear product photo"></div>
      <div class="gallery-tile" role="img" aria-label="Head protection product photo"></div>
    </div>
    <p class="para-one">Lorem ipsum dolor sit amet, consectetur adipisicing elit, sed do eiusmod tempor incididunt ut labore et dolore magna aliqua. Ut enim ad minim veniam, quis nostrud exercitation ullamco laboris nisi ut aliquip ex ea commodo consequat. Duis aute irure</p>
    <p class="para-two">Lorem ipsum dolor sit amet, consectetur adipisicing elit, sed do eiusmod tempor incididunt ut labore et dolore magna aliqua. Ut enim ad minim veniam, quis nostrud exercitation ullamco laboris nisi ut aliquip ex ea commodo consequat. Duis aute irure dolor in reprehenderit in voluptate velit esse cillum dolore eu fugiat.</p>
  </main>

  <aside class="whats-new">
    <h2>Whats new</h2>
    <article class="news-item" style="top:80px">
      <p class="news-date">Monday, 2013-09-12</p>
      <p class="news-text">Lorem ipsum dolor sit amet, consectetur adipisicing elit, sed do eiusmod tempor incididunt ut labore et dolore magna aliqua.</p>
      <p class="news-more">read more...</p>
    </article>
    <article class="news-item" style="top:206px">
      <p class="news-date">Monday, 2013-09-12</p>
      <p class="news-text">Lorem ipsum dolor sit amet, consectetur adipisicing elit, sed do eiusmod tempor incididunt ut labore et dolore magna aliqua.</p>
      <p class="news-more">read more...</p>
    </article>
    <article class="news-item" style="top:331px">
      <p class="news-date">Monday, 2013-09-12</p>
      <p class="news-text">Lorem ipsum dolor sit amet, consectetur adipisicing elit, sed do eiusmod tempor incididunt ut labore et dolore magna aliqua.</p>
      <p class="news-more">read more...</p>
    </article>
    <article class="news-item" style="top:456px">
      <p class="news-date">Monday, 2013-09-12</p>
      <p class="news-text">Lorem ipsum dolor sit amet, consectetur adipisicing elit, sed do eiusmod tempor incididunt ut labore et dolore magna aliqua.</p>
      <p class="news-more">read more...</p>
    </article>
  </aside>

  <footer class="site-footer">Copyright VELMAR 2013</footer>
</body>
</html>
```